Social Media Post Quote #3 - Native American Organization

- BLOSSOM - must be included
- Protect your community. Protect Your Elders. Stay Vaccinated. must be included
- Attached, company Logo, campaign logos and sample flu social media image. - our audience likes BRIGHT colors.
- Must include image from the United States, representing Land/Nature from one of the following regions, Plains and Woodlands, or Southwest, or Mountains, or Coast.
- must include quote: The well-being of our community’s mind, body, and spirit is sacred.
- One image will be provided three times - incorporating campaign logos - in some fashion
- For inspiration - https://dorvantek.org/ and https://www.pallorbook.com/Dorvantek

```html
<!DOCTYPE html>
<html lang="en">
<head>
<meta charset="utf-8">
<title>BLOSSOM – Quote Series</title>
<link rel="stylesheet" href="https://fonts.googleapis.com/css2?family=Barlow:wght@400;500&family=Barlow+Condensed:wght@300;400;700&family=Montserrat:wght@800&display=swap">
<style>
  :root {
    --page: #ffffff;
    --sky-top: #4f63a8;
    --sky-mid: #8a7fb8;
    --sunset: #f0a04a;
    --horizon: #c86a6a;
    --desert: #5f6a55;
    --mist: #efe3e3;
    --quote-fill: rgba(112, 72, 142, 0.58);
    --white: #ffffff;
    --brand-red: #b5473a;
    --brand-teal: #4aa8ae;
    --blossom-brown: #5a2e12;
    --blossom-teal: #49a9ae;
    --blossom-crimson: #9b1b2a;
  }
  * { box-sizing: border-box; margin: 0; padding: 0; }
  html, body { width: 1200px; height: 394px; overflow: hidden; background: var(--page); }
  .series { position: relative; width: 1200px; height: 394px; }
  .post {
    position: absolute; top: 0; width: 394px; height: 394px; overflow: hidden;
    font-family: "Barlow", sans-serif;
  }
  .post--flu { left: 4px; }
  .post--both { left: 403px; }
  .post--covid { left: 802px; }

  .landscape {
    position: absolute; inset: 0;
    background:
      linear-gradient(180deg, rgba(239,227,227,0) 0%, rgba(239,227,227,0) 66%, var(--mist) 82%, var(--mist) 100%),
      linear-gradient(180deg, var(--sky-top) 0%, var(--sky-mid) 30%, #a07ab0 40%, var(--horizon) 43%, var(--sunset) 46%, #8a6f9a 50%, var(--desert) 58%, #6f7566 68%, #a9a3a3 76%);
  }

  .headline {
    position: absolute; top: 19px; left: 0; right: 0;
    text-align: center; color: var(--white);
    font-size: 12.4px; font-weight: 400; letter-spacing: 0.1px; text-transform: uppercase;
  }
  .post--both .headline { font-size: 11.2px; }

  .quote-box {
    position: absolute; left: 63px; top: 108px; width: 276px; height: 140px;
    background: var(--quote-fill);
  }
  .quote-frame { position: absolute; left: 63px; top: 107px; width: 276px; height: 141px; overflow: visible; }
  .quote-mark {
    position: absolute; left: 170px; top: 70px; width: 60px; text-align: center;
    font-family: "Barlow Condensed", sans-serif; font-weight: 700;
    font-size: 104px; line-height: 1; color: var(--white);
  }
  .quote-text {
    position: absolute; left: 63px; top: 138px; width: 276px;
    text-align: center; color: var(--white);
    font-family: "Barlow Condensed", sans-serif; font-weight: 300;
    font-size: 28.5px; line-height: 25px; letter-spacing: -0.3px;
  }

  .campaign-name {
    position: absolute; left: 24px; top: 310px; width: 198px; height: 46px;
    display: flex; align-items: center; justify-content: center;
    font-family: "Montserrat", sans-serif; font-weight: 800; font-size: 30px; letter-spacing: 0.5px;
  }
  .post--flu .campaign-name { color: var(--blossom-brown); }
  .post--both .campaign-name { color: var(--blossom-teal); }
  .post--covid .campaign-name { color: var(--blossom-crimson); }

  .org {
    position: absolute; left: 246px; top: 325px; height: 20px;
    display: flex; align-items: center; gap: 7px;
  }
  .org__dot { width: 11px; height: 11px; border-radius: 50%; background: var(--brand-teal); }
  .org__name { color: var(--brand-red); font-weight: 500; font-size: 15px; letter-spacing: 0.4px; text-transform: uppercase; }

  .tagline {
    position: absolute; left: 0; right: 0; top: 364px; text-align: center;
    color: var(--brand-red); font-size: 10.6px; font-weight: 400; text-transform: uppercase;
  }
</style>
</head>
<body>
<main class="series">

  <article class="post post--flu">
    <div class="landscape" role="img" aria-label="Southwest desert at sunset with saguaro cacti under a purple and blue cloudy sky"></div>
    <p class="headline">Learn more about getting vaccinated against the flu</p>
    <div class="quote-box"></div>
    <svg class="quote-frame" viewBox="0 0 276 141" aria-hidden="true"><path d="M107 0.75 H0.75 V140.25 H275.25 V0.75 H169" fill="none" stroke="#fff" stroke-width="1.5"/></svg>
    <div class="quote-mark" aria-hidden="true">&ldquo;</div>
    <p class="quote-text">The well-being of our<br>community’s mind, body,<br>and spirit is sacred.</p>
    <div class="campaign-name">BLOSSOM</div>
    <div class="org"><span class="org__dot"></span><span class="org__name">Dorvantek</span></div>
    <p class="tagline">Protect your community. Protect your elders. Stay vaccinated.</p>
  </article>

  <article class="post post--both">
    <div class="landscape" role="img" aria-label="Southwest desert at sunset with saguaro cacti under a purple and blue cloudy sky"></div>
    <p class="headline">Learn more about getting vaccinated against COVID-19 &amp; the flu</p>
    <div class="quote-box"></div>
    <svg class="quote-frame" viewBox="0 0 276 141" aria-hidden="true"><path d="M107 0.75 H0.75 V140.25 H275.25 V0.75 H169" fill="none" stroke="#fff" stroke-width="1.5"/></svg>
    <div class="quote-mark" aria-hidden="true">&ldquo;</div>
    <p class="quote-text">The well-being of our<br>community’s mind, body,<br>and spirit is sacred.</p>
    <div class="campaign-name">BLOSSOM</div>
    <div class="org"><span class="org__dot"></span><span class="org__name">Dorvantek</span></div>
    <p class="tagline">Protect your community. Protect your elders. Stay vaccinated.</p>
  </article>

  <article class="post post--covid">
    <div class="landscape" role="img" aria-label="Southwest desert at sunset with saguaro cacti under a purple and blue cloudy sky"></div>
    <p class="headline">Learn more about getting vaccinated against COVID-19</p>
    <div class="quote-box"></div>
    <svg class="quote-frame" viewBox="0 0 276 141" aria-hidden="true"><path d="M107 0.75 H0.75 V140.25 H275.25 V0.75 H169" fill="none" stroke="#fff" stroke-width="1.5"/></svg>
    <div class="quote-mark" aria-hidden="true">&ldquo;</div>
    <p class="quote-text">The well-being of our<br>community’s mind, body,<br>and spirit is sacred.</p>
    <div class="campaign-name">BLOSSOM</div>
    <div class="org"><span class="org__dot"></span><span class="org__name">Dorvantek</span></div>
    <p class="tagline">Protect your community. Protect your elders. Stay vaccinated.</p>
  </article>

</main>
</body>
</html>
```